Box and label design for oil Tincture bottle

I need to design an attractive looking label for a 30ml CBD oil tincture along with designing a box for the tincture oil. I already have the logo (see attachment). I just need a nice, attractive looking artwork for the label and the box. The box is the standard 30ml tincture oil (see example attachment). The box has a total of 6 sides (4 on sides and 2 for top and bottom). Please include a section for supplemental facts and ingredients. Let's not focus to much on content. I am more concerned with design of box and label.
Target Market(s)
CBD customers
Look and feel
Each slider illustrates characteristics of the customer's brand and the style your logo design should communicate.

```html
<!DOCTYPE html>
<html lang="en">
<head>
<meta charset="utf-8">
<title>Bright Harbor CBD – Cannabis Tincture Label and Box</title>
<link href="https://fonts.googleapis.com/css2?family=Roboto+Condensed:wght@400;700&family=Zilla+Slab:wght@400;500&display=swap" rel="stylesheet">
<style>
  :root {
    --bg: #cbdae4;
    --brand-blue: #0e56a5;
    --deep-blue: #0a4791;
    --navy: #1a3c8c;
    --sky: #8fd2ec;
    --paper: #ffffff;
    --leaf-light: #3f7fc4;
  }
  * { margin: 0; padding: 0; box-sizing: border-box; }
  html, body { width: 1200px; height: 864px; overflow: hidden; }
  body {
    background: var(--bg);
    position: relative;
    font-family: "Roboto Condensed", sans-serif;
    color: var(--navy);
  }

  /* shared front content */
  .id-card {
    position: absolute;
    background: var(--paper);
    display: flex;
    flex-direction: column;
    align-items: center;
  }
  .brand { display: flex; flex-direction: column; align-items: center; }
  .brand-dot { border-radius: 50%; background: var(--brand-blue); }
  .brand-name {
    font-family: "Roboto Condensed", sans-serif;
    font-weight: 700;
    color: var(--navy);
    white-space: nowrap;
  }
  .product-kind {
    font-family: "Zilla Slab", serif;
    color: var(--navy);
    letter-spacing: 0.22em;
  }
  .product-name {
    font-family: "Roboto Condensed", sans-serif;
    font-weight: 700;
    color: var(--navy);
    line-height: 1;
  }
  .dose-band {
    position: absolute;
    left: 0; right: 0; bottom: 0;
    background: var(--sky);
    font-family: "Zilla Slab", serif;
    font-weight: 500;
    color: var(--navy);
    text-align: center;
  }
  .leaf-art {
    position: absolute;
    background: radial-gradient(ellipse at center, rgba(255,255,255,0.35), rgba(255,255,255,0) 70%);
  }

  /* bottle label */
  .label {
    position: absolute;
    left: 70px; top: 262px;
    width: 460px; height: 330px;
    background: var(--brand-blue);
  }
  .label .id-card { left: 150px; top: 0; width: 160px; height: 330px; padding-top: 40px; }
  .label .brand-dot { width: 26px; height: 26px; margin-bottom: 6px; }
  .label .brand-name { font-size: 14px; }
  .label .product-kind { font-size: 13px; margin-top: 28px; }
  .label .product-name { font-size: 26px; margin-top: 4px; }
  .label .dose-band { height: 28px; line-height: 28px; font-size: 10px; }
  .label .leaf-left { left: 20px; top: 70px; width: 110px; height: 200px; }
  .label .leaf-right { right: 20px; top: 90px; width: 110px; height: 200px; }

  /* box net */
  .box-top {
    position: absolute;
    left: 640px; top: 70px;
    width: 250px; height: 90px;
    background: var(--brand-blue);
    border: 6px solid var(--sky);
    border-bottom: none;
    display: flex; align-items: center; justify-content: center;
  }
  .box-top-mark {
    width: 70px; height: 30px;
    border: 2px solid var(--paper);
    border-radius: 50%;
  }
  .box-front {
    position: absolute;
    left: 640px; top: 160px;
    width: 250px; height: 620px;
    background: var(--brand-blue);
  }
  .box-front .id-card { left: 24px; top: 24px; width: 202px; height: 300px; padding-top: 40px; }
  .box-front .brand-dot { width: 38px; height: 38px; margin-bottom: 8px; }
  .box-front .brand-name { font-size: 19px; }
  .box-front .product-kind { font-size: 17px; margin-top: 36px; }
  .box-front .product-name { font-size: 36px; margin-top: 6px; }
  .box-front .dose-band { height: 36px; line-height: 36px; font-size: 13px; }
  .box-front .leaf-main { left: 10px; top: 340px; width: 230px; height: 270px; }

  .box-side {
    position: absolute;
    left: 890px; top: 160px;
    width: 170px; height: 620px;
    background: var(--paper);
    padding: 26px 18px;
    font-size: 10.5px;
    line-height: 1.45;
    color: var(--navy);
  }
  .info-title {
    font-weight: 700;
    font-size: 12px;
    text-transform: uppercase;
    letter-spacing: 0.04em;
    margin-bottom: 4px;
  }
  .info-block { margin-bottom: 18px; }
  .info-block p { margin: 0; }
  .box-side .leaf-side {
    left: 15px; bottom: 20px; width: 140px; height: 230px;
    background: radial-gradient(ellipse at center, rgba(63,127,196,0.28), rgba(63,127,196,0) 70%);
  }
</style>
</head>
<body>

  <section class="label" aria-label="Bottle label">
    <div class="leaf-art leaf-left" role="img" aria-label="Faint hemp leaf illustration"></div>
    <div class="leaf-art leaf-right" role="img" aria-label="Faint hemp leaf illustration"></div>
    <div class="id-card">
      <div class="brand">
        <span class="brand-dot"></span>
        <span class="brand-name">BRIGHT HARBOR CBD</span>
      </div>
      <span class="product-kind">CANNABIS</span>
      <span class="product-name">TINCTURE</span>
      <div class="dose-band">30 ml &nbsp;/&nbsp; 300mg of CBD</div>
    </div>
  </section>

  <div class="box-top"><span class="box-top-mark"></span></div>

  <section class="box-front" aria-label="Box front panel">
    <div class="id-card">
      <div class="brand">
        <span class="brand-dot"></span>
        <span class="brand-name">BRIGHT HARBOR CBD</span>
      </div>
      <span class="product-kind">CANNABIS</span>
      <span class="product-name">TINCTURE</span>
      <div class="dose-band">30 ml &nbsp;/&nbsp; 300mg of CBD</div>
    </div>
    <div class="leaf-art leaf-main" role="img" aria-label="Large line-drawn hemp leaf illustration"></div>
  </section>

  <section class="box-side" aria-label="Box side panel">
    <div class="info-block">
      <div class="info-title">Supplement Facts</div>
      <p>Serving size 1 ml</p>
      <p>Servings per container 30</p>
      <p>Hemp extract 10 mg</p>
    </div>
    <div class="info-block">
      <div class="info-title">Ingredients</div>
      <p>MCT oil, hemp extract, natural flavor.</p>
    </div>
    <div class="info-block">
      <div class="info-title">Directions</div>
      <p>Shake well. Hold 1 ml under tongue for 60 seconds.</p>
    </div>
    <div class="leaf-art leaf-side" role="img" aria-label="Hemp leaf line illustration"></div>
  </section>

</body>
</html>
```